Cafe Menu Required

We need a menu for our coffee shop.
I would like something very much the same as what I have attached.

I have attached a word doc with the items needed on the menu.

I have also attached our logo

I would like to print these on A3 size poster

Industry/Entity Type

Cafe

```html
<!DOCTYPE html>
<html lang="en">
<head>
<meta charset="utf-8">
<title>Remedy Canteen – Menu</title>
<link href="https://fonts.googleapis.com/css2?family=Graduate&family=Open+Sans:ital,wght@0,700;0,800;1,800&display=swap" rel="stylesheet">
<style>
  :root {
    --board: #3b3b3c;
    --board-dark: #2f2f30;
    --band: #c9cacc;
    --band-light: #dcdddf;
    --red: #e1232b;
    --white: #ffffff;
    --rule: rgba(255,255,255,0.22);
    --frame: #4a4a4a;
  }
  * { box-sizing: border-box; margin: 0; padding: 0; }
  html, body { width: 1200px; height: 848px; overflow: hidden; background: #fff; }
  .menu {
    position: relative; width: 1200px; height: 848px; overflow: hidden;
    background: radial-gradient(ellipse at 50% 55%, #454546 0%, var(--board) 55%, var(--board-dark) 100%);
    border: 3px solid var(--frame);
    font-family: "Open Sans", Arial, sans-serif; color: var(--white);
  }
  .top-band {
    position: absolute; left: 0; top: 0; width: 100%; height: 208px;
    background: linear-gradient(180deg, var(--band-light), var(--band));
    border-bottom: 2px solid #9a9b9d;
  }
  .photo {
    position: absolute; top: 14px; width: 216px; height: 176px; border-radius: 16px;
  }
  .photo--coffee { left: 3px; background: radial-gradient(circle at 45% 45%, #3a1f10 0%, #f3efe9 42%, #d9cfc2 100%); }
  .photo--latte { left: 238px; background: radial-gradient(circle at 50% 45%, #c9936a 0%, #a86a3e 40%, #f0ede8 58%, #6b5a4a 100%); }
  .photo--affogato { left: 730px; background: linear-gradient(180deg, #8a6a4c 0%, #efe9dc 35%, #2a1a12 60%, #4a3526 100%); }
  .photo--mango { left: 966px; background: radial-gradient(circle at 45% 55%, #ffc21a 0%, #f2a50c 50%, #8aa26a 100%); }
  .brand {
    position: absolute; left: 495px; top: 8px; width: 214px; height: 214px; border-radius: 50%;
    background: var(--white); border: 10px solid var(--red);
    display: flex; align-items: center; justify-content: center;
    box-shadow: 0 0 0 8px var(--band);
  }
  .brand-name { font-weight: 800; font-size: 38px; color: var(--red); letter-spacing: 1px; }
  .tagline {
    position: absolute; left: 0; top: 233px; width: 100%;
    display: flex; align-items: center; gap: 18px; padding: 0 4px;
    font-family: "Graduate", Georgia, serif; font-size: 35px; letter-spacing: 1px;
  }
  .tagline::before, .tagline::after { content: ""; flex: 1; height: 2px; background: #d0d0d0; }
  .section-tag {
    position: absolute; background: var(--red); padding: 4px 16px 6px 26px;
    transform: rotate(-4deg); clip-path: polygon(0 14%, 100% 0, 100% 100%, 2% 100%);
    font-weight: 800; font-style: italic; font-size: 23px; text-transform: uppercase; white-space: nowrap;
  }
  .tag-hot { left: 4px; top: 276px; }
  .tag-extras { left: 598px; top: 288px; }
  .tag-cold { left: 598px; top: 524px; }
  .item-list { position: absolute; list-style: none; }
  .item-list li {
    display: flex; align-items: center; border-bottom: 1px solid var(--rule);
    font-weight: 700; font-size: 15px;
  }
  .item-list .price { font-weight: 400; font-family: "Open Sans", Arial, sans-serif; }
  .list-hot { left: 32px; top: 336px; width: 505px; }
  .list-hot li { height: 28.3px; }
  .list-hot .name { width: 408px; }
  .list-extras { left: 622px; top: 334px; width: 520px; }
  .list-cold { left: 624px; top: 580px; width: 518px; }
  .list-extras li, .list-cold li { height: 30.3px; justify-content: space-between; padding-right: 8px; }
  .divider { position: absolute; left: 597px; top: 300px; width: 1px; height: 460px; background: rgba(255,255,255,0.1); }
  .beans {
    position: absolute; left: 0; bottom: 0; width: 100%; height: 92px;
    background: linear-gradient(180deg, rgba(120,30,10,0) 0%, #7a2410 35%, #4a150a 100%);
  }
</style>
</head>
<body>
<div class="menu">
  <div class="top-band"></div>
  <div class="photo photo--coffee" role="img" aria-label="Cup of black coffee on a saucer with coffee beans"></div>
  <div class="photo photo--latte" role="img" aria-label="Latte with heart latte art"></div>
  <div class="photo photo--affogato" role="img" aria-label="Iced coffee topped with a scoop of ice cream"></div>
  <div class="photo photo--mango" role="img" aria-label="Mango frappe garnished with mint"></div>
  <div class="brand"><span class="brand-name">REMEDY</span></div>

  <h1 class="tagline">COFFEE · CATERING · FOOD TO GO</h1>

  <h2 class="section-tag tag-hot">Hot Beverages</h2>
  <ul class="item-list list-hot">
    <li><span class="name">Espresso</span><span class="price">3.5</span></li>
    <li><span class="name">Piccolo</span><span class="price">3.5</span></li>
    <li><span class="name">Short Macchiato</span><span class="price">4.0</span></li>
    <li><span class="name">Long Macchiato</span><span class="price">4.5</span></li>
    <li><span class="name">Latte</span><span class="price">4/4.5/5.5</span></li>
    <li><span class="name">Cappucinno</span><span class="price">4/4.5/5.5</span></li>
    <li><span class="name">Flat White</span><span class="price">4/4.50/5.50</span></li>
    <li><span class="name">Long Black</span><span class="price">4/4.50/5.50</span></li>
    <li><span class="name">Hot Chocolate</span><span class="price">4/4.50/5.50</span></li>
    <li><span class="name">White Hot Chocolate</span><span class="price">4/4.50/5.50</span></li>
    <li><span class="name">Mocha</span><span class="price">4.5/5.0/6.0</span></li>
    <li><span class="name">White Choc Mocha</span><span class="price">4.5/5.0/6.0</span></li>
    <li><span class="name">Chai Latte</span><span class="price">4.5/5.0/6.0</span></li>
    <li><span class="name">Dirty Chai</span><span class="price">5.0/5.5/6.5</span></li>
    <li><span class="name">Selection of Teas</span><span class="price">3.8</span></li>
  </ul>

  <div class="divider"></div>

  <h2 class="section-tag tag-extras">Extras</h2>
  <ul class="item-list list-extras">
    <li><span class="name">Extra Shot</span><span class="price">0.5</span></li>
    <li><span class="name">Decaf</span><span class="price">0.5</span></li>
    <li><span class="name">Syrups - Caramel/Hazelnut/Vanilla</span><span class="price">0.5</span></li>
    <li><span class="name">Soy</span><span class="price">0.5</span></li>
    <li><span class="name">Lactose free</span><span class="price">0.5</span></li>
  </ul>

  <h2 class="section-tag tag-cold">Cold Beverages</h2>
  <ul class="item-list list-cold">
    <li><span class="name">Iced Latte</span><span class="price">4.5</span></li>
    <li><span class="name">Iced Long Black</span><span class="price">4.5</span></li>
    <li><span class="name">Iced Coffee w/ice cream</span><span class="price">6.0</span></li>
    <li><span class="name">Iced Chocolate w/ice cream</span><span class="price">6.0</span></li>
    <li><span class="name">Coffee Frappe</span><span class="price">6.0</span></li>
    <li><span class="name">Mango Frappe</span><span class="price">6.0</span></li>
  </ul>

  <div class="beans" role="img" aria-label="Row of roasted coffee beans along the bottom edge"></div>
</div>
</body>
</html>
```